Vantor Reach Unique Marketing Website Design

I am starting a new company that is a thought leader in the marketing consulting space. The company is called Vantor Reach. We intend to build a Wordpress site on the Astra Theme with the Spectra builder. Our goal is to become the leading voice that empowers high-ticket service business leaders to become Vantor Reach by equipping them with the cutting-edge frameworks and decision grade intelligence taught in leading business schools. What we are looking for is a website design that is clean and professional, making some use of white space well also being eye catching and distinctive in the consulting space. We will probably want to have a video on the homepage not in the hero section, but just below to explain the company and what we do. Our tagline is "Be found. Be chosen." I have attached a brand guide with some messaging, our typography choices, and our color system. The full site will have a primary nav that is four pages - About us, Services, Insights (essentially a blog), and Contact Us. The goal of this project is to develop an art direction that I can give to a designer to build loads of new pages.

Target Market(s)

Business owners (mostly male) from 30-60 years old, looking to fix their sales and marketing funnel.

Industry/Entity Type

Marketing consulting

Font styles to use
Sans Serif

Requirements
Must have
• A clean, professional design that builds trust with owners of high-ticket service businesses. We need a space for explainer video, and sections that tell prospects what we do. Would also like to have a blog carousel.
Nice to have
• Social feeds, if possible. See attached documents for colors and fonts.
Should not have
• Our feel is professional enough to be trustworthy, but unique enough to be memorable. Cartoon ideas do not meet the professional test, and we do not want the website to appear feminine.

```html
<!DOCTYPE html>
<html lang="en">
<head>
<meta charset="utf-8">
<title>Vantor Reach — Be Found. Be Chosen.</title>
<link rel="stylesheet" href="https://fonts.googleapis.com/css2?family=Bebas+Neue&family=Inter:wght@400;500;600;700;800&display=swap">
<style>
:root{
  --navy:#0b1631;
  --blue:#2f5cff;
  --green:#12b981;
  --purple:#8a5cf5;
  --red:#e5343a;
  --ink:#111827;
  --muted:#4b5563;
  --white:#ffffff;
  --footer:#1b1b1d;
  --line:#d6d9e0;
}
*{box-sizing:border-box;margin:0;padding:0}
html,body{width:1200px;height:3472px;overflow:hidden}
body{position:relative;font-family:"Inter",Arial,sans-serif;color:var(--ink);background:var(--white)}
.abs{position:absolute}
.display{font-family:"Bebas Neue","Oswald",Impact,sans-serif;font-weight:400;letter-spacing:.5px}
.accent{color:var(--blue)}
.bars{display:inline-block;width:7px;height:.8em;border-left:2px solid currentColor;border-right:2px solid currentColor;margin-right:10px;vertical-align:0}
.photo{position:absolute}
.btn{position:absolute;display:flex;align-items:stretch;background:var(--blue);color:var(--white);font-weight:700;font-size:11.5px;letter-spacing:.2px;text-transform:uppercase;white-space:nowrap}
.btn .label{flex:1;display:flex;align-items:center;padding-left:14px}
.btn .arrow{width:40px;display:flex;align-items:center;justify-content:center;border-left:2px solid rgba(255,255,255,.9);margin-left:4px;position:relative}
.btn .arrow::before{content:"";position:absolute;left:3px;top:4px;bottom:4px;border-left:1px solid rgba(255,255,255,.6)}
.btn.light{background:var(--white);color:var(--ink);border:1px solid var(--blue)}
.btn.light .arrow{border-left:2px solid var(--blue)}
.btn.light .arrow::before{border-left-color:var(--blue)}

.site-header{position:absolute;left:0;top:0;width:1200px;height:51px;background:var(--white)}
.brand{position:absolute;font-weight:800;font-size:22px;letter-spacing:-.3px;color:var(--navy)}
.nav{position:absolute;left:490px;top:20px;display:flex;gap:27px;font-size:11px;font-weight:700;color:var(--ink)}

.hero{position:absolute;left:0;top:51px;width:1200px;height:504px;background:var(--navy);overflow:hidden}
.hero-photo{left:520px;top:0;width:680px;height:504px;background:linear-gradient(90deg,var(--navy) 0%,#1d2f57 22%,#5a6a86 55%,#8a94a6 80%,#3e4c66 100%)}
.hero-title{position:absolute;left:142px;top:118px;color:var(--white);font-size:82px;line-height:86px}
.hero-rule{position:absolute;left:124px;top:132px;width:3px;height:180px;background:var(--white)}
.hero-sub{position:absolute;left:146px;top:296px;width:300px;color:var(--white);font-size:10px;line-height:15px}

.about-frame{left:121px;top:617px;width:364px;height:399px;border:5px solid var(--green);background:linear-gradient(160deg,#e9ecf1,#b9c0cc 55%,#5f6775)}
.about-inset{left:348px;top:731px;width:265px;height:217px;background:linear-gradient(135deg,#2a2620,#6b5a45 50%,#1c1e26)}
.about-mark{left:318px;top:651px;font-weight:700;font-size:17px;color:#b9bdc6}
.section-title{position:absolute;font-size:36px;line-height:40px;color:var(--ink)}
.about-copy{position:absolute;left:690px;top:718px;width:345px;font-size:10px;line-height:16px;color:var(--muted)}
.about-copy p{margin-bottom:17px}

.dark-band{position:absolute;left:0;top:1202px;width:1200px;height:708px;background:var(--navy)}
.not-row{position:absolute;left:121px;top:1135px;width:957px;height:137px;display:flex;gap:3px}
.not-card{flex:1;background:var(--white);border:1px solid var(--line);display:flex;flex-direction:column;align-items:center;padding-top:25px;text-align:center;font-size:15px;line-height:19px;font-weight:500;color:var(--ink)}
.not-card svg{margin-bottom:8px}

.pillar-sub{position:absolute;left:0;width:1200px;top:1373px;text-align:center;color:var(--white);font-size:11px}
.pillar{position:absolute;top:1414px;width:468px;height:433px;background:var(--green);color:var(--white)}
.pillar .photo{left:0;top:0;width:468px;height:235px}
.pillar-body{position:absolute;left:17px;top:255px;width:340px}
.pillar h3{font-size:24px;line-height:26px;margin-bottom:8px}
.pillar p{font-size:9.5px;line-height:15px;margin-bottom:8px}
.pillar b{font-size:15px;font-weight:700}

.video-band{position:absolute;left:0;top:1910px;width:1200px;height:348px;background:var(--blue)}
.video{left:140px;top:1973px;width:920px;height:412px;border:6px solid var(--white);background:linear-gradient(180deg,#c9ced6 0%,#8d95a3 45%,#3b3f46 85%,#24262b 100%)}

.blog-card{position:absolute;top:2510px;width:307px;height:340px;background:var(--purple);color:var(--white)}
.blog-card .photo{left:13px;top:13px;width:281px;height:203px}
.blog-card h4{position:absolute;left:13px;top:229px;right:14px;font-size:14.5px;line-height:18px;font-weight:700}
.blog-card p{position:absolute;left:13px;right:20px;font-size:9.5px;line-height:13px;color:#ece4ff}
.blog-card a{position:absolute;left:13px;top:309px;font-size:10px;font-weight:700;text-decoration:underline;color:var(--white)}
.carousel-arrow{position:absolute;top:2672px}
.ghost{position:absolute;left:0;width:1200px;top:2870px;text-align:center;font-weight:800;font-size:118px;letter-spacing:6px;color:#f2f4f9;line-height:110px;white-space:nowrap}

.cta{position:absolute;left:0;top:2975px;width:1200px;height:279px;background:var(--blue);color:var(--white);text-align:center}
.cta h2{position:absolute;left:0;width:1200px;top:52px;font-size:88px;line-height:88px;letter-spacing:1px}
.cta p{position:absolute;left:0;width:1200px;top:139px;font-size:15px}

.footer{position:absolute;left:0;top:3254px;width:1200px;height:218px;background:var(--footer);color:#b8bac0}
.footer-brand{position:absolute;left:123px;top:30px;width:197px;height:35px;background:var(--white);color:var(--navy);font-weight:800;font-size:22px;display:flex;align-items:center;justify-content:center}
.footer-about{position:absolute;left:123px;top:84px;width:245px;font-size:8.5px;line-height:14px;color:#9ea1a8}
.footer h5{position:absolute;top:30px;font-family:"Bebas Neue","Oswald",sans-serif;font-weight:400;font-size:15px;letter-spacing:1.2px;color:var(--white)}
.footer-links{position:absolute;left:437px;top:62px;font-size:9px;line-height:21.5px;list-style:none;color:#9ea1a8}
.contact-row,.social-row{position:absolute;display:flex;align-items:center;gap:12px;font-size:9px;color:#9ea1a8}
.footer-div{position:absolute;top:26px;width:1px;height:150px;background:#2d2e32}
.copyright{position:absolute;left:0;width:1200px;top:190px;text-align:center;font-size:8.5px;color:#8d9097;border-top:1px solid #2d2e32;padding-top:8px}
</style>
</head>
<body>

<header class="site-header">
  <div class="brand" style="left:121px;top:13px">VANTOR REACH</div>
  <nav class="nav"><span>ABOUT US</span><span>SERVICES</span><span>INSIGHT</span></nav>
  <div class="btn" style="left:938px;top:8px;width:140px;height:35px">
    <span class="label">CONTACT US</span>
    <span class="arrow"><svg width="13" height="11" viewBox="0 0 13 11"><path d="M1 5.5h11M7 1l5 4.5L7 10" fill="none" stroke="#fff" stroke-width="1.3"/></svg></span>
  </div>
</header>

<section class="hero">
  <div class="photo hero-photo" role="img" aria-label="Two consultants in suits reviewing a laptop in a bright office corridor"></div>
  <div class="abs" style="left:1068px;top:0;width:3px;height:170px;background:#fff"></div>
  <div class="hero-rule"></div>
  <h1 class="hero-title display">BE FOUND.<br>BE <span class="accent">CHOSEN.</span></h1>
  <p class="hero-sub">Decision-grade marketing strategy for high-ticket service businesses that want predictable, scalable demand.</p>
  <div class="btn" style="left:144px;top:353px;width:213px;height:41px">
    <span class="label">EXPLORE OUR APPROACH</span>
    <span class="arrow"><svg width="13" height="11" viewBox="0 0 13 11"><path d="M1 5.5h11M7 1l5 4.5L7 10" fill="none" stroke="#fff" stroke-width="1.3"/></svg></span>
  </div>
</section>

<section class="about">
  <div class="photo about-frame" role="img" aria-label="Consultant presenting to a seated team in a meeting room"></div>
  <div class="abs about-mark">VANTOR REACH</div>
  <div class="photo about-inset" role="img" aria-label="Laptop showing analytics dashboards on a desk"></div>
  <h2 class="section-title display" style="left:688px;top:673px"><span class="bars"></span>ABOUT VANTOR <span class="accent">REACH</span></h2>
  <div class="about-copy">
    <p>Vantor Reach is a playbook-as-a-service consultancy that teaches high-ticket service businesses to understand why qualified buyers don't choose them—and design buying experiences where reaching full commitment is the natural conclusion.</p>
    <p>We apply the tools of Choice Design and Signal Insight to diagnose revenue problems and design solutions.</p>
    <p>The business model is a product company with consulting as a complementary premium tier.</p>
  </div>
  <div class="btn" style="left:690px;top:906px;width:202px;height:40px">
    <span class="label">LEARN MORE ABOUT US</span>
    <span class="arrow"><svg width="13" height="11" viewBox="0 0 13 11"><path d="M1 5.5h11M7 1l5 4.5L7 10" fill="none" stroke="#fff" stroke-width="1.3"/></svg></span>
  </div>
</section>

<div class="dark-band"></div>

<section class="not">
  <h2 class="section-title display" style="left:0;width:1200px;text-align:center;top:1071px"><span class="bars"></span>WHAT VANTOR <span class="accent">REACH</span> IS NOT</h2>
  <div class="not-row">
    <div class="not-card"><svg width="46" height="46" viewBox="0 0 46 46"><circle cx="23" cy="23" r="22" fill="var(--red)"/><circle cx="23" cy="23" r="13" fill="#fff"/><path d="M18 18l10 10M28 18l-10 10" stroke="var(--red)" stroke-width="4" stroke-linecap="round"/></svg>A marketing<br>consultancy per se</div>
    <div class="not-card"><svg width="46" height="46" viewBox="0 0 46 46"><circle cx="23" cy="23" r="22" fill="var(--red)"/><circle cx="23" cy="23" r="13" fill="#fff"/><path d="M18 18l10 10M28 18l-10 10" stroke="var(--red)" stroke-width="4" stroke-linecap="round"/></svg>A funnel Agency</div>
    <div class="not-card"><svg width="46" height="46" viewBox="0 0 46 46"><circle cx="23" cy="23" r="22" fill="var(--red)"/><circle cx="23" cy="23" r="13" fill="#fff"/><path d="M18 18l10 10M28 18l-10 10" stroke="var(--red)" stroke-width="4" stroke-linecap="round"/></svg>A sales<br>Enablement Firm</div>
    <div class="not-card"><svg width="46" height="46" viewBox="0 0 46 46"><circle cx="23" cy="23" r="22" fill="var(--red)"/><circle cx="23" cy="23" r="13" fill="#fff"/><path d="M18 18l10 10M28 18l-10 10" stroke="var(--red)" stroke-width="4" stroke-linecap="round"/></svg>An<br>Execution Partner</div>
    <div class="not-card"><svg width="46" height="46" viewBox="0 0 46 46"><circle cx="23" cy="23" r="22" fill="var(--red)"/><circle cx="23" cy="23" r="13" fill="#fff"/><path d="M18 18l10 10M28 18l-10 10" stroke="var(--red)" stroke-width="4" stroke-linecap="round"/></svg>A time-for<br>Money Advisory</div>
  </div>
</section>

<section class="pillars">
  <h2 class="section-title display" style="left:0;width:1200px;text-align:center;top:1329px;color:#fff"><span class="bars"></span>THE TWO <span class="accent">PILLARS</span></h2>
  <p class="pillar-sub">Vantor Reach' methodology rests on two complementary disciplines:</p>
  <article class="pillar" style="left:123px">
    <div class="photo" role="img" aria-label="Analyst reviewing bar charts on a laptop and tablet" style="background:linear-gradient(120deg,#5b4a36,#a8825a 45%,#2b2a30)"></div>
    <div class="pillar-body">
      <h3 class="display">SIGNAL INSIGHT</h3>
      <p><b>Definition:</b> The discipline of discovering and diagnosing what's actually happening in a buyer's journey—before prescribing solutions.</p>
      <p><b>Metaphor:</b> Reconnaissance. Gathering intel on the battlefield before making strategic decisions.</p>
      <p><b>Output:</b> A dossier—a clear-eyed assessment of reality, not assumptions</p>
    </div>
  </article>
  <article class="pillar" style="left:609px">
    <div class="photo" role="img" aria-label="Wooden letter blocks spelling principles on infographic printouts beside a keyboard" style="background:linear-gradient(120deg,#5d6068,#c9b99c 45%,#e7e3dc)"></div>
    <div class="pillar-body">
      <h3 class="display">CHOICE DESIGN</h3>
      <p><b>Definition:</b> The discipline of applying behavioral science principles to design buying experiences where saying yes feels safer than saying no.</p>
      <p><b>Metaphor:</b> Decision architecture. Engineering the environment in which high-stakes choices get made.</p>
      <p><b>Output:</b> A design system—principles and architecture for what to build, not just tactics to try.</p>
    </div>
  </article>
</section>

<section class="video-section">
  <div class="video-band"></div>
  <div class="photo video" role="img" aria-label="Explainer video cover: business team gathered around a laptop"></div>
  <svg class="abs" style="left:575px;top:2157px" width="50" height="50" viewBox="0 0 50 50"><circle cx="25" cy="25" r="24" fill="#fff" fill-opacity=".55"/><circle cx="25" cy="25" r="18" fill="#fff"/><path d="M20 16l13 9-13 9z" fill="var(--blue)"/></svg>
</section>

<section class="blog">
  <div class="ghost">VANTOR REACH</div>
  <h2 class="section-title display" style="left:0;width:1200px;text-align:center;top:2446px">LATEST <span class="accent">BLOG</span></h2>
  <svg class="carousel-arrow" style="left:86px" width="16" height="16" viewBox="0 0 16 16"><circle cx="8" cy="8" r="7" fill="none" stroke="#222" stroke-width="1"/><path d="M11 8H5M7.5 5.5L5 8l2.5 2.5" fill="none" stroke="#222" stroke-width="1"/></svg>
  <svg class="carousel-arrow" style="left:1096px" width="16" height="16" viewBox="0 0 16 16"><circle cx="8" cy="8" r="7" fill="none" stroke="#222" stroke-width="1"/><path d="M5 8h6M8.5 5.5L11 8l-2.5 2.5" fill="none" stroke="#222" stroke-width="1"/></svg>

  <article class="blog-card" style="left:123px">
    <div class="photo" role="img" aria-label="Row of wooden figures with a red arrow pointing to a single red figure" style="background:linear-gradient(135deg,#a9dbe4,#7fc3d0 60%,#e8e3da)"></div>
    <h4>Demand Is Not Leads</h4>
    <p style="top:252px">Why most high-ticket service businesses chase activity instead of real demand—and how that mistake limits growth.</p>
    <a>LEARN MORE</a>
  </article>
  <article class="blog-card" style="left:448px">
    <div class="photo" role="img" aria-label="Two colleagues discussing charts at a desk with a laptop" style="background:linear-gradient(135deg,#6d6a63,#b7b2a8 50%,#dcd9d2)"></div>
    <h4>Why Most Marketing Advice<br>Fails Service Businesses</h4>
    <p style="top:270px">What works in ecommerce and SaaS often breaks in high-consideration, high-trust sales environments.</p>
    <a>LEARN MORE</a>
  </article>
  <article class="blog-card" style="left:772px">
    <div class="photo" role="img" aria-label="Two professionals reviewing a tablet in a modern office" style="background:linear-gradient(135deg,#8a6a4a,#c7a27a 45%,#3b4456)"></div>
    <h4>How Buyers Actually Choose<br>Service Providers</h4>
    <p style="top:270px">A clearer mental model for understanding buyer decisions in complex, competitive markets.</p>
    <a>LEARN MORE</a>
  </article>

  <div class="btn" style="left:516px;top:2881px;width:169px;height:39px">
    <span class="label">VIEW ALL BLOG</span>
    <span class="arrow"><svg width="13" height="11" viewBox="0 0 13 11"><path d="M1 5.5h11M7 1l5 4.5L7 10" fill="none" stroke="#fff" stroke-width="1.3"/></svg></span>
  </div>
</section>

<section class="cta">
  <h2 class="display">READY TO STOP GUESSING?</h2>
  <p>If you're serious about building predictable demand, let's talk.</p>
  <div class="btn light" style="left:489px;top:175px;width:222px;height:39px">
    <span class="label">CONTACT VANTOR REACH</span>
    <span class="arrow"><svg width="13" height="11" viewBox="0 0 13 11"><path d="M1 5.5h11M7 1l5 4.5L7 10" fill="none" stroke="var(--blue)" stroke-width="1.3"/></svg></span>
  </div>
</section>

<footer class="footer">
  <div class="footer-brand">VANTOR REACH</div>
  <p class="footer-about">Vantor Reach is a playbook-as-a-service consultancy that teaches high-ticket service businesses to understand why qualified buyers don't choose them—and design buying experiences where reaching full commitment is the natural conclusion.</p>
  <div class="footer-div" style="left:386px"></div>
  <div class="footer-div" style="left:634px"></div>
  <div class="footer-div" style="left:876px"></div>

  <h5 style="left:437px">MAIN LINKS</h5>
  <ul class="footer-links"><li>About us</li><li>Services</li><li>Insights</li><li>Contact Us.</li></ul>

  <h5 style="left:656px">CONTACT US</h5>
  <div class="contact-row" style="left:656px;top:62px">
    <svg width="24" height="24" viewBox="0 0 24 24"><circle cx="12" cy="12" r="11" fill="none" stroke="#fff" stroke-width="1"/><path d="M8.5 7.5l2 0 1 2.5-1.3 1a6 6 0 0 0 3 3l1-1.3 2.5 1v2a1 1 0 0 1-1 1A8.5 8.5 0 0 1 7.5 8.5a1 1 0 0 1 1-1z" fill="#fff"/></svg>1-800-555-0142</div>
  <div class="contact-row" style="left:656px;top:96px">
    <svg width="24" height="24" viewBox="0 0 24 24"><circle cx="12" cy="12" r="11" fill="none" stroke="#fff" stroke-width="1"/><rect x="7" y="8.5" width="10" height="7" fill="#fff"/><path d="M7 8.5l5 4 5-4" fill="none" stroke="var(--footer)" stroke-width="1"/></svg><span style="color:var(--blue)">hello@vantorreach.com</span></div>

  <h5 style="left:958px">FOLLOW US</h5>
  <div class="social-row" style="left:958px;top:62px"><svg width="24" height="24" viewBox="0 0 24 24"><circle cx="12" cy="12" r="11" fill="none" stroke="#fff" stroke-width="1"/></svg>Community</div>
  <div class="social-row" style="left:958px;top:96px"><svg width="24" height="24" viewBox="0 0 24 24"><circle cx="12" cy="12" r="11" fill="none" stroke="#fff" stroke-width="1"/></svg>Updates</div>
  <div class="social-row" style="left:958px;top:131px"><svg width="24" height="24" viewBox="0 0 24 24"><circle cx="12" cy="12" r="11" fill="none" stroke="#fff" stroke-width="1"/></svg>Network</div>

  <div class="copyright">© Copyright 2026 Vantor Reach All Rights Reserved.</div>
</footer>

</body>
</html>
```